Dorsey K. Wendell Business Card

We need a business card for our company Dorsey K. Wendell Heating & Plumbing to be distributed to potential customers. It should follow the color scheme of our logo and have a modern upscale and masculine look.

The logo is attached and the info below should also be included:

5187 W. Cedar Brook Rd.
Manheim, PA 17545

Russell T. Wendell
(717) 592-0817
russelltwendell@fernmail.net
dorseykwendell.net
PA #093148

Industry/Entity Type

Business

Contact Information for Business Card

5187 W. Cedar Brook Rd.
Manheim, PA 17545

Russell T. Wendell
(717) 592-0817
russelltwendell@fernmail.net
dorseykwendell.net
PA #093148

Colors

Designer to choose colors to be used in the design.

Requirements
Must have
• Information above included

```html
<!DOCTYPE html>
<html lang="en">
<head>
<meta charset="utf-8">
<title>Dorsey K. Wendell Business Card</title>
<link rel="stylesheet" href="https://fonts.googleapis.com/css2?family=Lato:wght@400;700&family=Montserrat:wght@600;800&display=swap">
<style>
  :root {
    --page-bg: #2b2b2d;
    --blue-light: #1d86d0;
    --blue-mid: #1466b8;
    --blue-deep: #0a4a96;
    --panel: rgba(6, 40, 92, 0.28);
    --white: #ffffff;
  }
  * { margin: 0; padding: 0; box-sizing: border-box; }
  html, body { width: 1200px; height: 791px; overflow: hidden; }
  body {
    background: var(--page-bg);
    position: relative;
    font-family: "Lato", sans-serif;
    color: var(--white);
  }
  .card {
    position: absolute;
    left: 300px;
    width: 600px;
    height: 343px;
    background: radial-gradient(ellipse at 55% 50%, var(--blue-light) 0%, var(--blue-mid) 55%, var(--blue-deep) 100%);
    box-shadow: 0 12px 28px rgba(0, 0, 0, 0.55);
  }
  .card--front { top: 32px; }
  .card--back { top: 416px; }
  .texture-panel {
    position: absolute;
    background: var(--panel);
  }
  .card--front .texture-panel { left: 40px; top: 30px; right: 40px; bottom: 30px; }
  .card--back .texture-panel { left: 40px; top: 36px; width: 300px; bottom: 36px; }
  .brand {
    position: absolute;
    display: flex;
    align-items: center;
    gap: 12px;
    font-family: "Montserrat", sans-serif;
    font-weight: 800;
    text-transform: uppercase;
    color: var(--white);
    white-space: nowrap;
  }
  .brand__square {
    width: 44px;
    height: 44px;
    background: var(--white);
    flex: none;
  }
  .brand__name { line-height: 1.15; letter-spacing: 0.5px; }
  .brand__name span { display: block; }
  .card--front .brand { left: 50%; top: 50%; transform: translate(-50%, -50%); font-size: 28px; }
  .card--front .brand__square { width: 58px; height: 58px; }
  .card--back .brand { left: 190px; top: 50%; transform: translate(-50%, -50%); font-size: 19px; gap: 10px; }
  .card--back .brand__name { font-size: 19px; }
  .brand__trade { font-size: 0.55em; letter-spacing: 2px; }
  .contact {
    position: absolute;
    left: 372px;
    top: 58px;
    width: 220px;
  }
  .contact__name {
    font-family: "Montserrat", sans-serif;
    font-weight: 600;
    font-size: 20px;
    margin-bottom: 24px;
  }
  .contact__address {
    font-weight: 700;
    font-size: 14px;
    line-height: 1.35;
    font-style: normal;
    margin-bottom: 14px;
  }
  .contact__license { font-size: 13px; margin-bottom: 12px; }
  .contact__list { list-style: none; font-size: 13px; }
  .contact__list li { display: flex; align-items: center; gap: 8px; line-height: 1.55; }
  .contact__icon { width: 13px; height: 13px; flex: none; }
</style>
</head>
<body>
  <section class="card card--front" aria-label="Card front">
    <div class="texture-panel" role="img" aria-label="Fine diagonal line texture panel"></div>
    <div class="brand">
      <div class="brand__square"></div>
      <div class="brand__name">
        <span>Dorsey K. Wendell</span>
        <span class="brand__trade">Heating &amp; Plumbing</span>
      </div>
    </div>
  </section>

  <section class="card card--back" aria-label="Card back">
    <div class="texture-panel" role="img" aria-label="Fine diagonal line texture panel"></div>
    <div class="brand">
      <div class="brand__square"></div>
      <div class="brand__name">
        <span>Dorsey K. Wendell</span>
        <span class="brand__trade">Heating &amp; Plumbing</span>
      </div>
    </div>
    <div class="contact">
      <h1 class="contact__name">Russell T. Wendell</h1>
      <address class="contact__address">5187 W. Cedar Brook Rd.<br>Manheim, PA 17545</address>
      <p class="contact__license">PA #093148</p>
      <ul class="contact__list">
        <li>
          <svg class="contact__icon" viewBox="0 0 16 16" aria-hidden="true"><path fill="#fff" d="M3.5 1.5l2.5 3-1.5 1.5c.8 1.8 2.2 3.2 4 4l1.5-1.5 3 2.5-1.5 2.5C6.5 13.5 2.5 9.5 1 3z"/></svg>
          (717) 592-0817
        </li>
        <li>
          <svg class="contact__icon" viewBox="0 0 16 16" aria-hidden="true"><rect x="1" y="3" width="14" height="10" fill="none" stroke="#fff" stroke-width="1.5"/><path d="M1 3l7 6 7-6" fill="none" stroke="#fff" stroke-width="1.5"/></svg>
          russelltwendell@fernmail.net
        </li>
        <li>
          <svg class="contact__icon" viewBox="0 0 16 16" aria-hidden="true"><rect x="1" y="2" width="14" height="9" fill="none" stroke="#fff" stroke-width="1.5"/><path d="M5 14h6M8 11v3" stroke="#fff" stroke-width="1.5"/></svg>
          dorseykwendell.net
        </li>
      </ul>
    </div>
  </section>
</body>
</html>
```